Law Office needs stationery design and business card

I currently have been using the same letterhead for the last 8 years. Since i 'm about to adding another location, I want to revamp my letterhead and business card. I already have a logo i'm happy with. I will upload my current letterhead, fax sheet, envelope, and logos. I need a business card also. I have 2 locations, 1 phone number, 1 fax line, website, etc. If possible and fitting with the design, I would like to keep the same information listed currently on the letterhead.

**Keep in mind, I also NEED A FAX SHEET COVER. thank you

Hello, Please submit a Gray Scale or Black and White version of your designs also, since most of the time I will be printing NON color stationery. I will seldom use a color print for my letterhead, I would like to have a color version for my benefit, however i will print in grayscale majority of the time . For the Business Card, that can just be in color. When I get my business cards they will be in color.Thank youEnrique Added Sunday, September 18, 2016

```html
<!DOCTYPE html>
<html lang="en">
<head>
<meta charset="utf-8">
<title>Marchetti Law – Business Card</title>
<link rel="stylesheet" href="https://fonts.googleapis.com/css2?family=Libre+Franklin:wght@400;500;600&display=swap">
<style>
  :root {
    --backdrop: #3b3531;
    --card: #1b1b1b;
    --card-edge: #111111;
    --gold: #c9a45c;
    --white: #f2f2f2;
    --muted: #bdbdbd;
    --divider: #6c6c6c;
  }
  * { box-sizing: border-box; margin: 0; padding: 0; }
  html, body {
    width: 1200px; height: 787px; overflow: hidden;
    background: var(--backdrop);
    font-family: "Libre Franklin", Arial, sans-serif;
  }
  .canvas {
    position: relative; width: 1200px; height: 787px;
  }
  .card {
    position: absolute;
    width: 540px; height: 309px;
    background: var(--card);
    border: 1px solid var(--card-edge);
    box-shadow: 0 10px 28px rgba(0,0,0,.45);
  }
  .card-front { left: 40px; top: 120px; }
  .card-back  { left: 620px; top: 358px; }

  /* Front */
  .front-mark {
    position: absolute; left: 150px; top: 62px;
    display: flex; align-items: center; gap: 16px;
  }
  .mark-square {
    width: 58px; height: 58px; background: var(--gold);
  }
  .front-name {
    color: var(--white); font-weight: 500;
    font-size: 26px; letter-spacing: 3px;
  }
  .front-web {
    position: absolute; left: 30px; top: 180px;
    color: var(--white); font-size: 13px; letter-spacing: 5px;
  }

  /* Back */
  .back-identity {
    position: absolute; left: 40px; top: 68px; width: 230px;
    text-align: center;
  }
  .back-square {
    width: 38px; height: 38px; background: var(--gold);
    margin: 0 auto 12px;
  }
  .firm-name {
    color: var(--gold); font-weight: 500;
    font-size: 22px; letter-spacing: 2px;
  }
  .attorney-name {
    color: var(--gold); font-weight: 600;
    font-size: 17px; margin-top: 18px;
  }
  .attorney-title {
    color: var(--white); font-size: 13px; margin-top: 4px;
  }
  .back-divider {
    position: absolute; left: 292px; top: 48px;
    width: 1px; height: 210px; background: var(--divider);
  }
  .contact-list {
    position: absolute; left: 312px; top: 58px;
    list-style: none;
  }
  .contact-item {
    display: flex; align-items: flex-start; gap: 10px;
    color: var(--white); font-size: 13px; line-height: 17px;
    margin-bottom: 5px;
  }
  .contact-item svg { flex: 0 0 14px; width: 14px; height: 16px; fill: var(--gold); margin-top: 1px; }
  .social-square { flex: 0 0 12px; width: 12px; height: 12px; background: var(--gold); margin: 2px 1px 0; }
</style>
</head>
<body>
<div class="canvas">

  <section class="card card-front" aria-label="Business card front">
    <div class="front-mark">
      <div class="mark-square"></div>
      <span class="front-name">MARCHETTI LAW</span>
    </div>
    <p class="front-web">www.MarchettiLaw.com</p>
  </section>

  <section class="card card-back" aria-label="Business card back">
    <div class="back-identity">
      <div class="back-square"></div>
      <p class="firm-name">MARCHETTILAW</p>
      <p class="attorney-name">Gustavo Marchetti Esq.</p>
      <p class="attorney-title">Attorney</p>
    </div>
    <div class="back-divider"></div>
    <ul class="contact-list">
      <li class="contact-item">
        <svg viewBox="0 0 14 16"><path d="M7 0a5.5 5.5 0 0 0-5.5 5.5C1.5 9.6 7 16 7 16s5.5-6.4 5.5-10.5A5.5 5.5 0 0 0 7 0zm0 7.6a2.1 2.1 0 1 1 0-4.2 2.1 2.1 0 0 1 0 4.2z"/></svg>
        <span>48 Alder Row<br>Suite 210, Fairmont, PA 19120</span>
      </li>
      <li class="contact-item">
        <svg viewBox="0 0 14 16"><path d="M7 0a5.5 5.5 0 0 0-5.5 5.5C1.5 9.6 7 16 7 16s5.5-6.4 5.5-10.5A5.5 5.5 0 0 0 7 0zm0 7.6a2.1 2.1 0 1 1 0-4.2 2.1 2.1 0 0 1 0 4.2z"/></svg>
        <span>907 Linden Ave<br>Halberg, PA 19055</span>
      </li>
      <li class="contact-item">
        <svg viewBox="0 0 14 16"><path d="M1 4c0-1.5 2.5-2.5 6-2.5S13 2.5 13 4v1.5H10V4.2H4V5.5H1zM3 7h8l2 7H1zm4 1.6a2 2 0 1 0 0 4 2 2 0 0 0 0-4z"/></svg>
        <span>610.555.0184</span>
      </li>
      <li class="contact-item">
        <svg viewBox="0 0 14 16"><path d="M3.5 0h7A1.5 1.5 0 0 1 12 1.5v13a1.5 1.5 0 0 1-1.5 1.5h-7A1.5 1.5 0 0 1 2 14.5v-13A1.5 1.5 0 0 1 3.5 0zM3.6 2v10.5h6.8V2zM7 13.2a.9.9 0 1 0 0 1.8.9.9 0 0 0 0-1.8z"/></svg>
        <span>484.555.0127</span>
      </li>
      <li class="contact-item">
        <svg viewBox="0 0 14 16"><path d="M0 4h14v9H0zm1.2 1.2v.4L7 9.3l5.8-3.7v-.4zm0 1.8v4.8h11.6V7L7 10.8z"/></svg>
        <span>Gustavo@MarchettiLaw.com</span>
      </li>
      <li class="contact-item">
        <span class="social-square"></span>
        <span>MarchettiLaw</span>
      </li>
    </ul>
  </section>

</div>
</body>
</html>
```